Affiliate website design and wireframe

We need a design of an affiliate website for an application we purchased, it is important that you build the website pages according to the developer of the applications specifications (please see attached documents) the developer of the application will configure the pages and add them to the site. Please take special note of his comments below.

We all so need you to create a wire frame so the developer can test everything (http://sketchwire.tolvaro.vn/)

It will be the homepage and about 16 inner pages (please see attached files)
Here is our website http://bluvendmarket.com/affiliate/affiliates/index.php

The version of the software we purchased is the Kivo Partner Hubline version

Comments from the developers

1. I will need the source files of the design (photoshop .psd files and font files if custom fonts are used), since the implementation is closely bound to component sizes (like border width, margin width etc.) and colors. If you own a corporate design manual, it's crucial to send it as well. Also, please, make sure if you use custom fonts, that these allow legal website integration (like google web fonts).

2. Any and every content is controlled via templates. All editing/adding/removing etc. is done here. The template files are essentially html/php documents, they use a template engine called quillo (http://www.quillo.net/) which has it's own language similar to php.

3. .psd files are ideal, because we deal with the specifics of KPX/KPH implementation on a daily basis. Any html/css developed in advance may prove to be a poor choice. You may choose to let an in-house developer do the job, but experience wise this is more costly, since he will not be accustomed to the template/functionality systems of KPX/KPH.

4. I will need the source files of the design (photoshop .psd files and font files if custom fonts are used), since the implementation is closely bound to component sizes (like border width, margin width etc.) and colors. If you own a corporate design manual, it's crucial to send it as well. Also, please, make sure if you use custom fonts, that these allow legal website integration (like google web fonts).

Regards,

Dorek Hanval
Multimedia Design

We prefer illustrations more than pictures of real people.

This is the home page, it is asking for Merchant and Affiliate sign up, not just affiliate.

http://bluvendmarket.com/affiliate/index.php

Please note the home page features both Merchant and Affiliate sign up

We are looking for illustration design not just stock images

Please remember the search menu that searches for the available programs, see the example we gave you, look at the search menu at the top of the page http://www.tradelumo.com/

We are reviewing everything, no need to send more designs

Target Market(s)

Natural Products Manufacturers
Natural products Sales reps
Natural Products Bloggers
Social Marketing

Industry/Entity Type

Software

Requirements
Must have
• 1. All links on pages should go to the appropriate pages.
2. Colors can be based on our logo design (look at the attachments)
3. Here is our website http://bluvendmarket.com/affiliate/affiliates/index.php
4. We have attached a drawing of how we think the homepage concept should follow.
5. Main concept of design, is trying to show our sales people (Affiliates) are doing multiple things to advertise and sell the merchants products.(see logo)
6. Need to be able to edit all text and images.
7. Our target audience is Natural product sales people (Advertisers, bloggers, ext) and natural product manufacturers.
8. You can speak to the company who made the application, through live chat, on there website http://www.kivopartnerhubline.com/
Nice to have
• See Attached Documents.
site should take up whole website pages
Look For fun Illustrated Website, one of the better ones we have seen is http://www.tradelumo.com/index.cfm
Should not have
• Please look very carefully at developers comment above.

```html
<!DOCTYPE html>
<html lang="en">
<head>
<meta charset="utf-8">
<title>BluVendMarket – Affiliate Program</title>
<link href="https://fonts.googleapis.com/css2?family=Roboto:ital,wght@0,300;0,400;0,500;0,700;1,400;1,700&family=Roboto+Condensed:wght@400;700&display=swap" rel="stylesheet">
<style>
  :root {
    --navy: #1f3a5d;
    --navy-dark: #172838;
    --footer: #1f3446;
    --green: #4f9a12;
    --green-logo: #5aa419;
    --lime: #9cb82a;
    --yellow: #f7c52b;
    --coral: #f0504f;
    --steel: #3a6891;
    --hero-bg: #eeeeee;
    --feature-bg: #f3f3f3;
    --text-grey: #9a9a9a;
    --text-dark: #555;
    --white: #ffffff;
  }
  * { box-sizing: border-box; margin: 0; padding: 0; }
  html, body { width: 723px; height: 1200px; overflow: hidden; }
  body { position: relative; font-family: 'Roboto', sans-serif; background: var(--white); color: var(--text-dark); }
  .abs { position: absolute; }

  /* top bar */
  .topbar { left: 0; top: 0; width: 723px; height: 22px; background: var(--navy); color: var(--white); font-size: 7.5px; font-weight: 500; }
  .topbar .welcome { left: 79px; top: 7px; }
  .topbar .login-link { top: 7px; display: flex; align-items: center; gap: 4px; }
  .topbar .search-field { left: 545px; top: 3px; width: 84px; height: 16px; background: #e8ecf0; border-radius: 2px 0 0 2px; }
  .topbar .search-btn { left: 629px; top: 3px; width: 19px; height: 16px; background: #16304d; border-radius: 0 2px 2px 0; display: flex; align-items: center; justify-content: center; }

  /* header */
  .header { left: 0; top: 22px; width: 723px; height: 47px; background: var(--white); border-bottom: 1px solid #e4e4e4; }
  .logo { left: 77px; top: 10px; display: flex; align-items: center; gap: 5px; font-family: 'Roboto Condensed', sans-serif; font-weight: 700; font-size: 24px; color: var(--green-logo); letter-spacing: -0.5px; }
  .logo .mark { width: 10px; height: 10px; background: var(--green-logo); }
  .nav a { position: absolute; top: 16px; font-size: 11px; color: var(--navy); text-decoration: none; }
  .nav .active { color: var(--green); }
  .nav .underline { position: absolute; left: 501px; top: 45px; width: 41px; height: 2px; background: var(--green); }

  /* hero */
  .hero { left: 0; top: 69px; width: 723px; height: 270px; background: linear-gradient(180deg, #f4f4f4, #e9e9e9); }
  .hero-card { top: 75px; width: 156px; height: 159px; padding: 26px 16px 0 17px; color: var(--white); }
  .hero-card.signup { left: 75px; background: var(--navy); }
  .hero-card.login { left: 240px; background: var(--green); }
  .hero-card .kicker { font-family: 'Roboto Condensed', sans-serif; font-weight: 700; font-size: 10px; line-height: 1; }
  .hero-card .headline { font-family: 'Roboto Condensed', sans-serif; font-weight: 700; font-size: 17px; line-height: 1.1; margin-bottom: 11px; }
  .hero-card p { font-size: 7.5px; line-height: 1.35; letter-spacing: -0.1px; }
  .hero-card .btn { position: absolute; top: 118px; height: 27px; display: flex; align-items: center; justify-content: center; font-size: 7.5px; font-weight: 500; color: var(--white); text-transform: uppercase; }
  .hero-card.signup .btn { left: 34px; width: 92px; background: var(--coral); }
  .hero-card.login .btn { left: 33px; width: 91px; background: var(--yellow); }
  .hero-illustration { left: 396px; top: 120px; width: 252px; height: 219px; background: radial-gradient(ellipse at 60% 55%, #2b4f7a 0%, #8aa7c2 45%, rgba(230,230,230,0) 75%); }

  /* features */
  .features { left: 0; top: 339px; width: 723px; height: 207px; background: var(--feature-bg); }
  .feature { top: 0; width: 190px; text-align: center; }
  .feature .icon { margin: 25px auto 0; width: 40px; height: 40px; }
  .feature h3 { margin-top: 15px; font-size: 10px; font-weight: 400; color: var(--navy); line-height: 1.3; letter-spacing: -0.2px; }
  .feature p { margin-top: 11px; font-size: 6.6px; font-weight: 300; color: var(--text-grey); line-height: 1.55; padding: 0 4px; }
  .divider { top: 0; width: 2px; height: 207px; background: #e3e3e3; }
  .divider .accent { position: absolute; left: 0; bottom: 0; width: 2px; height: 50px; background: var(--steel); }

  /* how it works */
  .how { left: 0; top: 546px; width: 723px; height: 332px; background: linear-gradient(160deg, #3a3d40 0%, #262829 60%, #2f3336 100%); border-top: 3px solid var(--steel); }
  .how h2 { position: absolute; left: 0; top: 26px; width: 723px; text-align: center; color: var(--white); font-size: 17px; font-weight: 700; }
  .how .lead { position: absolute; left: 110px; top: 52px; width: 503px; text-align: center; color: var(--white); font-size: 7px; font-weight: 700; font-style: italic; line-height: 1.3; text-transform: uppercase; }
  .step { width: 171px; height: 93px; background: linear-gradient(180deg, #ffffff, #ececec); text-align: center; padding: 27px 20px 0; font-size: 8px; line-height: 1.3; color: var(--text-dark); }
  .step .num { position: absolute; left: 68px; top: -18px; width: 35px; height: 35px; border-radius: 50%; background: var(--steel); color: var(--white); font-size: 19px; font-weight: 500; display: flex; align-items: center; justify-content: center; }

  /* join */
  .join { left: 0; top: 878px; width: 723px; height: 144px; background: var(--lime); text-align: center; }
  .join h2 { position: absolute; left: 0; top: 24px; width: 723px; font-size: 15px; font-weight: 700; color: #1a1a1a; }
  .join .lead { position: absolute; left: 94px; top: 49px; width: 535px; color: var(--white); font-size: 7px; font-style: italic; line-height: 1.35; text-transform: uppercase; }
  .join .btn { position: absolute; left: 255px; top: 86px; width: 213px; height: 38px; background: var(--navy); color: var(--white); font-size: 16px; font-weight: 500; display: flex; align-items: center; justify-content: center; }

  /* footer */
  .footer { left: 0; top: 1022px; width: 723px; height: 128px; background: var(--footer); color: #d8dee4; }
  .footer-col { top: 27px; }
  .footer-col h4 { font-size: 8.5px; font-weight: 400; margin-bottom: 10px; color: #e8ecf0; }
  .footer-col li { list-style: none; font-size: 7px; line-height: 11.6px; display: flex; align-items: center; gap: 3px; }
  .footer-col li::before { content: ""; width: 5px; height: 5px; border: 1px solid #d8dee4; border-radius: 50%; }
  .store-badge { top: 52px; width: 63px; height: 20px; border-radius: 2px; }
  .store-badge.ios { left: 501px; background: #1e88e5; }
  .store-badge.android { left: 569px; background: #ef7b3a; }

  .bottombar { left: 0; top: 1150px; width: 723px; height: 50px; background: var(--navy-dark); color: #8c9aa8; font-size: 7px; }
  .bottombar .copy { left: 77px; top: 21px; display: flex; gap: 9px; }
  .social { top: 11px; width: 27px; height: 27px; border-radius: 50%; background: #2f8fd8; }
</style>
</head>
<body>

  <div class="abs topbar">
    <span class="abs welcome">Default welcome msg!</span>
    <span class="abs login-link" style="left:394px">
      <svg width="8" height="8" viewBox="0 0 10 10"><rect x="1" y="2" width="7" height="7" fill="none" stroke="#fff" stroke-width="1.2"/><path d="M4 6 L9 1" stroke="#fff" stroke-width="1.2"/></svg>
      Affiliate login
    </span>
    <span class="abs login-link" style="left:472px">
      <svg width="8" height="8" viewBox="0 0 10 10"><circle cx="5" cy="3" r="2.3" fill="#fff"/><path d="M1 10 Q5 4 9 10 Z" fill="#fff"/></svg>
      Merchant login
    </span>
    <div class="abs search-field"></div>
    <div class="abs search-btn">
      <svg width="9" height="9" viewBox="0 0 10 10"><circle cx="4" cy="4" r="3" fill="none" stroke="#fff" stroke-width="1.3"/><path d="M6.2 6.2 L9 9" stroke="#fff" stroke-width="1.5"/></svg>
    </div>
  </div>

  <div class="abs header">
    <div class="abs logo"><span>BLUVENDMARKET</span><span class="mark"></span></div>
    <nav class="nav">
      <a class="active" style="left:509px">Home</a>
      <a style="left:551px">Sign up</a>
      <a style="left:602px">Contact us</a>
      <span class="underline"></span>
    </nav>
  </div>

  <section class="abs hero">
    <div class="abs hero-card signup">
      <div class="kicker">START MAKING</div>
      <div class="headline">MONEY NOW!</div>
      <p>There is no charge to join our Affiliate Program. We pay commissions for all sales you referred. Earn up to 30% commissions</p>
      <a class="btn">Affiliates signup</a>
    </div>
    <div class="abs hero-card login">
      <div class="kicker">ALREADY</div>
      <div class="headline">OUR AFFILIATE?</div>
      <p>We have always something new for our affiliates. Login to check earned commissions and new campaigns.</p>
      <a class="btn">Login</a>
    </div>
    <div class="abs hero-illustration" role="img" aria-label="Illustration of a salesman in a suit juggling text, blog, email, social and phone icons in front of a city skyline"></div>
  </section>

  <section class="abs features">
    <div class="abs feature" style="left:56px">
      <svg class="icon" viewBox="0 0 40 40"><circle cx="17" cy="11" r="6" fill="#3c3c3c"/><path d="M5 34 Q6 20 17 20 Q26 20 27 27 L27 34 Z" fill="#3c3c3c"/><circle cx="29" cy="28" r="7" fill="#3c3c3c" stroke="#f3f3f3" stroke-width="1.5"/><text x="29" y="32" text-anchor="middle" font-family="Roboto, sans-serif" font-weight="700" font-size="10" fill="#fff">$</text></svg>
      <h3>Earn up to 50% commission for all products!</h3>
      <p>Not only can you join our team and help spread the word about your favorite products, you can get rewarded for your efforts. Our system tracks referrals and pays top commissions for every client you send our way.</p>
    </div>
    <div class="abs divider" style="left:264px"><span class="accent"></span></div>
    <div class="abs feature" style="left:267px">
      <svg class="icon" viewBox="0 0 40 40"><circle cx="15" cy="15" r="9" fill="#3c3c3c"/><text x="15" y="19" text-anchor="middle" font-family="Roboto, sans-serif" font-weight="700" font-size="11" fill="#fff">$</text><circle cx="25" cy="25" r="9" fill="#3c3c3c" stroke="#f3f3f3" stroke-width="1.5"/><text x="25" y="29" text-anchor="middle" font-family="Roboto, sans-serif" font-weight="700" font-size="11" fill="#fff">€</text></svg>
      <h3>High Conversion Rate = More Money.</h3>
      <p>Our website and plans generate one of the highest conversion rates in the industry. Our high conversion rates mean that the people who you send here are more likely to buy our products. Of course we can't prove that either, but if you don't trust us, why would you want to refer people here?</p>
    </div>
    <div class="abs divider" style="left:461px"><span class="accent"></span></div>
    <div class="abs feature" style="left:467px">
      <svg class="icon" viewBox="0 0 40 40"><circle cx="20" cy="22" r="14" fill="none" stroke="#3c3c3c" stroke-width="3.5"/><rect x="17" y="3" width="6" height="4" fill="#3c3c3c"/><path d="M20 22 L14 14" stroke="#3c3c3c" stroke-width="3" stroke-linecap="round"/></svg>
      <h3>Long cookie duration.</h3>
      <p>If a customer comes from your site to ours, and then comes back to purchase six months later, you get credit.</p>
    </div>
  </section>

  <section class="abs how" role="img" aria-label="Dimmed photo background of business charts and a hand with a pen">
    <h2>HOW DOES IT WORK?</h2>
    <p class="lead">It couldn't be simpler! We've streamlined our entire affiliate process to ensure ease of use, while still maintaining extremely accurate affiliate tracking. The process is as follows:</p>
    <div class="abs step" style="left:82px;top:95px"><span class="num">1</span>Visitor clicks on an affiliate link on your site or in an email.</div>
    <div class="abs step" style="left:277px;top:95px"><span class="num">2</span>The visitors IP is logged and a cookie is placed in their browser for tracking purposes.</div>
    <div class="abs step" style="left:471px;top:95px"><span class="num">3</span>The visitor browses our site, and may decide to order.</div>
    <div class="abs step" style="left:82px;top:215px;padding-left:14px;padding-right:14px"><span class="num">4</span>If the visitor orders (the order need not be placed during the same browser session--cookies and IPs are stored indefinitely), the order will be registered as a sale for you</div>
    <div class="abs step" style="left:277px;top:215px"><span class="num">5</span>We will review and approve the sale.</div>
    <div class="abs step" style="left:471px;top:215px"><span class="num">6</span>You will receive commission payouts.</div>
  </section>

  <section class="abs join">
    <h2>READY TO JOIN?</h2>
    <p class="lead">It couldn't be simpler! We've streamlined our entire affiliate process to ensure ease of use, while still maintaining extremely accurate affiliate tracking. The process is as follows:</p>
    <a class="btn">JOIN NOW!</a>
  </section>

  <footer class="abs footer">
    <div class="abs footer-col" style="left:82px">
      <h4>About us</h4>
      <ul><li>Company</li><li>Contact us</li><li>Privacy Policy</li></ul>
    </div>
    <div class="abs footer-col" style="left:223px">
      <h4>Affiliates</h4>
      <ul><li>Affiliates information</li><li>Affiliate link formats</li></ul>
    </div>
    <div class="abs footer-col" style="left:377px">
      <h4>Affiliates</h4>
      <ul><li>Merchants Login</li><li>Integration methods</li><li>API Reference</li><li>Samples and Tests</li><li>Kivo Partner Pro</li></ul>
    </div>
    <div class="abs footer-col" style="left:501px">
      <h4>Mobile</h4>
    </div>
    <div class="abs store-badge ios"></div>
    <div class="abs store-badge android"></div>
  </footer>

  <div class="abs bottombar">
    <div class="abs copy"><span>© 2014 bluvendmarket.com All rights reserved</span><span>Terms of Service</span><span>Privacy Policy</span></div>
    <span class="abs social" style="left:558px"></span>
    <span class="abs social" style="left:587px"></span>
    <span class="abs social" style="left:616px"></span>
  </div>

</body>
</html>
```